Website Header for new website

We need a header/banner design for our revised website. Here is the link to our existing website lorimakwell.me and to our new website in process agewiseplus.us
Area of expertise is older adults, baby boomers and caregivers
This is an individual, professional website for a Speaker, Keynoter, Author, Brocaster

Target Market(s)

Event planners, broadcasters, publishers

Font styles to use
Serif

```html
<!DOCTYPE html>
<html lang="en">
<head>
<meta charset="UTF-8">
<title>Lori Makwell — Speaker, Author, Broadcaster</title>
<link href="https://fonts.googleapis.com/css2?family=Playfair+Display:wght@500&family=Roboto:wght@400;500&display=swap" rel="stylesheet">
<style>
  :root {
    --wordmark: #1f2a44;
    --accent-blue: #4a4cf0;
    --nav-text: #2b2f3a;
    --white: #ffffff;
    --hero-dark: #06061a;
    --hero-mid: #1a1a6e;
    --hero-glow: #2f2fb8;
    --jacket: #d8321a;
    --skirt: #3a2a26;
    --box-text: #333333;
  }
  * { margin: 0; padding: 0; box-sizing: border-box; }
  html, body { width: 1200px; height: 501px; overflow: hidden; background: var(--white); }
  body { position: relative; font-family: "Roboto", Arial, sans-serif; }

  .site-header {
    position: absolute; left: 0; top: 0; width: 1200px; height: 73px;
    background: var(--white); z-index: 2;
  }
  .site-logo {
    position: absolute; left: 86px; top: 22px;
    font-family: "Roboto", Arial, sans-serif; font-weight: 500;
    font-size: 24px; line-height: 28px; color: var(--wordmark);
  }
  .main-nav {
    position: absolute; right: 85px; top: 28px;
    display: flex; gap: 35px; list-style: none;
    font-size: 12.5px; color: var(--nav-text);
  }
  .main-nav li { display: flex; align-items: center; gap: 6px; white-space: nowrap; }
  .main-nav svg { width: 10px; height: 6px; }

  .hero {
    position: absolute; left: 0; top: 73px; width: 1200px; height: 428px;
    overflow: hidden;
  }
  .hero-backdrop {
    position: absolute; inset: 0;
    background:
      radial-gradient(ellipse 60% 40% at 55% 10%, var(--hero-glow) 0%, transparent 70%),
      linear-gradient(180deg, var(--hero-mid) 0%, #0d0b35 35%, var(--hero-dark) 100%);
  }
  .speaker-portrait {
    position: absolute; left: 86px; top: 60px; width: 244px; height: 368px;
    border-radius: 110px 110px 0 0;
    background: linear-gradient(180deg, #c9a77a 0%, #c9a77a 22%, var(--jacket) 24%, #b82815 70%, var(--skirt) 72%, #1e1614 100%);
  }
  .hero-name {
    position: absolute; left: 390px; top: 126px;
    font-family: "Playfair Display", Georgia, serif; font-weight: 500;
    font-size: 42px; line-height: 56px; color: var(--white);
    display: flex; align-items: center; gap: 22px;
  }
  .hero-name::after {
    content: ""; width: 64px; height: 2px; background: var(--accent-blue);
  }
  .role-list {
    position: absolute; left: 390px; top: 208px;
    display: grid; grid-template-columns: 251px 200px; row-gap: 14px;
    list-style: none; color: var(--white); font-size: 17px;
  }
  .role-list li { display: flex; align-items: center; gap: 10px; height: 23px; white-space: nowrap; }
  .role-list li::before {
    content: ""; width: 4px; height: 4px; border-radius: 50%; background: var(--accent-blue);
  }

  .featured-label {
    position: absolute; left: 911px; top: 124px;
    color: var(--white); font-size: 10px; font-weight: 500; letter-spacing: 3px;
  }
  .outlet {
    position: absolute; background: var(--white);
    display: flex; align-items: center; justify-content: center; text-align: center;
    font-size: 10px; font-weight: 500; color: var(--box-text); line-height: 1.1;
  }
</style>
</head>
<body>
  <header class="site-header">
    <div class="site-logo">Lori Makwell</div>
    <ul class="main-nav">
      <li>Home</li>
      <li>Meet Lori</li>
      <li>Speaker/Spokesperson
        <svg viewBox="0 0 10 6"><path d="M1 1l4 4 4-4" fill="none" stroke="#4a7bd0" stroke-width="1"/></svg>
      </li>
      <li>Blog</li>
      <li>Podcast</li>
      <li>Books</li>
      <li>Work with Lori</li>
      <li>Contact</li>
      <li>Press</li>
    </ul>
  </header>

  <section class="hero">
    <div class="hero-backdrop" role="img" aria-label="Photo of a large conference hall filled with an audience under blue stage lights"></div>
    <div class="speaker-portrait" role="img" aria-label="Photo of the speaker in a red jacket and patterned skirt"></div>

    <h1 class="hero-name">Lori Makwell</h1>
    <ul class="role-list">
      <li>Dynamic Keynoter</li>
      <li>Prolific Author</li>
      <li>Motivating Speaker</li>
      <li>Entertaining Blogger</li>
      <li>Influential Broadcaster</li>
      <li>Effective Trainer</li>
    </ul>

    <div class="featured-label">FEATURED ON:</div>
    <div class="outlet" style="left:913px;top:156px;width:106px;height:42px;">MoneyNet</div>
    <div class="outlet" style="left:913px;top:207px;width:43px;height:42px;">Biz Air</div>
    <div class="outlet" style="left:964px;top:207px;width:55px;height:42px;">Metro Talk</div>
    <div class="outlet" style="left:913px;top:259px;width:106px;height:43px;">City 570</div>
    <div class="outlet" style="left:1032px;top:156px;width:82px;height:68px;">Daytime Talk</div>
    <div class="outlet" style="left:1032px;top:233px;width:82px;height:69px;">Eastline Audio</div>
  </section>
</body>
</html>
```